QUIVL Systems website

We need a website design using much of the information on the QUIVL flyer (attached) we just had a PixelMarsh designer create. We'd like a WordPress Site, no need for a shopping cart attached to it. It should have an About us page, Book titles page, a blog page, Membership and Navigators pages contact us and privacy policy and terms of services.

Coding

Coded - Design and coding required

```html
<!DOCTYPE html>
<html lang="en">
<head>
<meta charset="utf-8">
<title>QUIVL Systems</title>
<link href="https://fonts.googleapis.com/css2?family=Poppins:wght@400;500;600;700&family=Open+Sans:wght@400;600&display=swap" rel="stylesheet">
<style>
:root{
  --blue:#2f5596;
  --blue-dark:#24467e;
  --ink:#222831;
  --text:#5a5f66;
  --muted:#8a8f96;
  --light:#f6f7f9;
  --footer:#1f2a3c;
  --footer-deep:#1a2333;
  --white:#ffffff;
  --red:#e0414d;
  --green:#1f8a3c;
  --amber:#f2a825;
  --olive:#a28b14;
  --teal:#159a86;
}
*{margin:0;padding:0;box-sizing:border-box}
html,body{width:1200px;height:2843px;overflow:hidden}
body{position:relative;background:var(--white);font-family:'Open Sans',Arial,sans-serif;color:var(--text)}
.abs{position:absolute}
.backdrop{position:absolute;left:0;top:0}
h1,h2,h3,h4{font-family:'Poppins',Arial,sans-serif}

/* header */
.site-header{position:absolute;left:0;top:0;width:1200px;height:72px;background:var(--white);box-shadow:0 1px 4px rgba(0,0,0,.08);z-index:2}
.brand{position:absolute;left:134px;top:18px;font:700 26px 'Poppins',Arial,sans-serif;color:var(--blue);letter-spacing:1px}
.brand-mark{position:absolute;left:160px;top:8px;width:10px;height:10px;border-radius:50%;background:var(--blue)}
.header-rule{position:absolute;left:258px;top:0;width:1px;height:72px;background:#e6e8eb}
.main-nav{position:absolute;left:349px;top:29px}
.main-nav a{font:600 12px 'Poppins',Arial,sans-serif;color:var(--ink);text-decoration:none;text-transform:uppercase;position:absolute;white-space:nowrap}
.main-nav a.active::after{content:"";position:absolute;left:0;right:0;bottom:-10px;height:2px;background:var(--blue)}
.header-phone{position:absolute;left:928px;top:22px;font:700 15px 'Poppins',Arial,sans-serif;color:var(--blue);display:flex;align-items:center;gap:14px}
.header-divider{position:absolute;left:912px;top:0;width:1px;height:72px;background:#e6e8eb}

/* hero */
.hero-title{position:absolute;left:0;width:1200px;top:212px;text-align:center;font:700 36px/44px 'Poppins',Arial,sans-serif;color:var(--white);text-transform:uppercase;letter-spacing:.5px}
.hero-sub{position:absolute;left:0;width:1200px;top:320px;text-align:center;font:400 15px 'Poppins',Arial,sans-serif;color:var(--white)}
.btn{position:absolute;display:flex;align-items:center;justify-content:center;font:500 11px 'Poppins',Arial,sans-serif;text-transform:uppercase;text-decoration:none}
.btn-blue{background:var(--blue);color:var(--white)}
.btn-white{background:var(--white);color:var(--blue);font-weight:600;font-size:12px}
.hero-arrow{position:absolute;top:280px;width:26px;height:26px;border-radius:50%;background:rgba(255,255,255,.55)}

/* pillars */
.section-title{position:absolute;left:0;width:1200px;text-align:center;font:700 20px 'Poppins',Arial,sans-serif}
.intro{position:absolute;left:390px;width:420px;top:718px;text-align:center;font-size:11px;line-height:24px;color:var(--muted)}
.pillar{position:absolute;top:786px;width:200px;text-align:center}
.pillar svg{display:block;margin:0 auto}
.pillar-caption{margin-top:20px;font:600 11px/20px 'Poppins',Arial,sans-serif;color:var(--ink)}

/* story */
.story-photo{position:absolute;left:139px;top:1126px;width:374px;height:272px;background:linear-gradient(135deg,#dfe6ef,#9fb2c9 55%,#c7b3a4);box-shadow:0 2px 6px rgba(0,0,0,.15)}
.story-title{position:absolute;left:549px;top:1124px;font:700 19px 'Poppins',Arial,sans-serif;color:var(--ink)}
.story-text{position:absolute;left:549px;top:1166px;width:518px;font-size:11px;line-height:24px;color:var(--muted)}
.story-text p+p{margin-top:4px}

/* membership */
.member-title{position:absolute;left:0;width:1200px;top:1514px;text-align:center;font:700 20px 'Poppins',Arial,sans-serif;color:var(--white)}
.member-sub{position:absolute;left:0;width:1200px;top:1545px;text-align:center;font:400 14px 'Poppins',Arial,sans-serif;color:var(--white)}
.offer{position:absolute;top:1608px;width:292px}
.offer-photo{height:136px}
.offer h3{margin:18px 0 10px 4px;font:600 14px 'Poppins',Arial,sans-serif;color:var(--white);text-transform:uppercase}
.offer ul{list-style:none;margin-left:22px}
.offer li{font-size:11px;line-height:25px;color:var(--white);position:relative;padding-left:20px}
.offer li::before{content:"";position:absolute;left:2px;top:8px;width:7px;height:4px;border-left:2px solid var(--white);border-bottom:2px solid var(--white);transform:rotate(-45deg)}

/* blog */
.blog-card{position:absolute;top:2099px;width:290px}
.blog-photo{height:162px}
.blog-card h3{margin:14px 0 10px;font:600 14px 'Poppins',Arial,sans-serif;color:var(--ink)}
.blog-card p{font-size:11px;line-height:24px;color:var(--muted)}

/* footer */
.quote-bar{position:absolute;left:134px;top:2423px;width:933px;height:88px;background:var(--blue)}
.quote-label{position:absolute;left:74px;top:27px;font:600 12px/16px 'Poppins',Arial,sans-serif;color:var(--white);letter-spacing:1px;text-transform:uppercase}
.quote-phone{position:absolute;left:240px;top:20px;font:700 31px 'Poppins',Arial,sans-serif;color:var(--white);letter-spacing:1px}
.subscribe-field{position:absolute;left:516px;top:29px;width:254px;height:32px;border-radius:16px;background:var(--white);font-size:10px;color:#a0a5ab;padding:9px 0 0 40px}
.subscribe-btn{position:absolute;left:785px;top:29px;width:126px;height:32px;border-radius:16px;background:var(--footer);color:var(--white);font:600 12px 'Poppins',Arial,sans-serif;display:flex;align-items:center;justify-content:center}
.footer-col{position:absolute;top:2566px}
.footer-col h4{font:600 13px 'Poppins',Arial,sans-serif;color:var(--white);margin-bottom:18px}
.footer-links{list-style:none}
.footer-links li{font-size:11px;line-height:29px;color:#b9c0cb;position:relative;padding-left:22px}
.footer-links li::before{content:"›";position:absolute;left:0;color:#7f8896}
.office li{list-style:none;display:flex;gap:18px;font-size:11px;line-height:20px;color:#b9c0cb;margin-bottom:14px}
.office svg{flex:none;margin-top:3px}
.social{display:flex;gap:8px}
.social span{width:24px;height:24px;display:block}
.copyright{position:absolute;left:0;top:2801px;width:1200px;height:42px;background:var(--footer-deep);text-align:center;font-size:10px;line-height:42px;color:#7f8896}
</style>
</head>
<body>

<svg class="backdrop" width="1200" height="2843" viewBox="0 0 1200 2843" aria-hidden="true">
  <defs>
    <linearGradient id="heroTone" x1="0" y1="0" x2="1" y2="1">
      <stop offset="0" stop-color="#8d97a6"/>
      <stop offset=".5" stop-color="#5f6c80"/>
      <stop offset="1" stop-color="#3d4658"/>
    </linearGradient>
    <linearGradient id="bandTone" x1="0" y1="0" x2="1" y2="1">
      <stop offset="0" stop-color="#3a66a6"/>
      <stop offset="1" stop-color="#2c528f"/>
    </linearGradient>
  </defs>
  <path d="M0,1040 C300,1010 700,1090 1200,1030 V620 H0 Z" fill="var(--light)"/>
  <path d="M0,1480 C240,1420 400,1480 700,1440 C900,1415 1050,1430 1200,1410 V1960 C1000,1990 800,1950 500,1990 C300,2015 150,2030 0,2020 Z" fill="url(#bandTone)"/>
  <path d="M0,2480 C200,2420 700,2440 1200,2375 V2843 H0 Z" fill="var(--footer)"/>
</svg>

<header class="site-header">
  <span class="brand-mark"></span>
  <span class="brand">QUIVL</span>
  <span class="header-rule"></span>
  <nav class="main-nav">
    <a class="active" style="left:0">Home</a>
    <a style="left:67px">About us</a>
    <a style="left:162px">Blog</a>
    <a style="left:230px">Membership</a>
    <a style="left:339px">Privacy Policy</a>
    <a style="left:467px">Contact us</a>
  </nav>
  <span class="header-divider"></span>
  <div class="header-phone">
    <svg width="16" height="16" viewBox="0 0 24 24"><path d="M6.6 10.8a15.1 15.1 0 0 0 6.6 6.6l2.2-2.2c.3-.3.7-.4 1-.2 1.1.4 2.3.6 3.6.6.6 0 1 .4 1 1V20c0 .6-.4 1-1 1A17 17 0 0 1 3 4c0-.6.4-1 1-1h3.5c.6 0 1 .4 1 1 0 1.3.2 2.5.6 3.6.1.3 0 .7-.2 1z" fill="var(--blue)"/></svg>
    <span style="margin-left:6px">833-555-0147</span>
  </div>
</header>

<svg class="abs" style="left:0;top:72px" width="1200" height="560" viewBox="0 72 1200 560" role="img" aria-label="Photo of business people meeting around a laptop in an office">
  <path d="M0,72 H1200 V548 C900,590 450,565 200,600 C110,612 50,622 0,618 Z" fill="url(#heroTone)"/>
</svg>
<div class="hero-arrow" style="left:96px"></div>
<div class="hero-arrow" style="left:1074px"></div>
<h1 class="hero-title">Accurate your business<br>with QUIVL</h1>
<p class="hero-sub">A Simple Comprehensive Coaching System for Small Business</p>
<a class="btn btn-blue" style="left:561px;top:368px;width:111px;height:33px">Read more</a>

<h2 class="section-title" style="top:672px;color:var(--blue)">QUIVL = Strategy, Team, Action, Accountability, Results</h2>
<p class="intro">Business consulting excepteur sint occaecat cupidatat consulting non proident, sunt in culpa qui officia deserunt laborum Market.</p>

<svg class="abs" style="left:198px;top:850px" width="780" height="2" aria-hidden="true"><line x1="0" y1="1" x2="780" y2="1" stroke="#d5d9de" stroke-dasharray="3 4"/></svg>

<div class="pillar" style="left:98px">
  <svg width="116" height="128" viewBox="0 0 116 128"><polygon points="58,4 112,34 112,94 58,124 4,94 4,34" fill="#fff" stroke="var(--red)" stroke-width="4"/><circle cx="58" cy="52" r="12" fill="none" stroke="var(--ink)" stroke-width="3"/><circle cx="58" cy="52" r="5" fill="var(--red)"/><text x="58" y="89" text-anchor="middle" font-family="Poppins,Arial,sans-serif" font-weight="700" font-size="12" fill="var(--ink)">STRATEGY</text></svg>
  <p class="pillar-caption">Long-Term Vision,<br>Tatical Planning</p>
</div>
<div class="pillar" style="left:299px">
  <svg width="116" height="128" viewBox="0 0 116 128"><polygon points="58,4 112,34 112,94 58,124 4,94 4,34" fill="#fff" stroke="var(--green)" stroke-width="4"/><circle cx="46" cy="44" r="5" fill="var(--green)"/><circle cx="58" cy="42" r="6" fill="var(--green)"/><circle cx="70" cy="44" r="5" fill="var(--green)"/><path d="M38 62c0-8 5-11 8-11s8 3 8 11zM48 62c0-10 5-13 10-13s10 3 10 13zM62 62c0-8 5-11 8-11s8 3 8 11z" fill="var(--green)"/><text x="58" y="89" text-anchor="middle" font-family="Poppins,Arial,sans-serif" font-weight="700" font-size="12" fill="var(--ink)">TEAM</text></svg>
  <p class="pillar-caption">Healthy Team Relationship<br>&amp; Development</p>
</div>
<div class="pillar" style="left:503px">
  <svg width="116" height="128" viewBox="0 0 116 128"><polygon points="58,4 112,34 112,94 58,124 4,94 4,34" fill="#fff" stroke="var(--amber)" stroke-width="4"/><rect x="54" y="38" width="7" height="24" rx="3.5" fill="var(--amber)"/><path d="M50 40a9 9 0 0 1 15 0" fill="none" stroke="var(--amber)" stroke-width="2"/><text x="58" y="89" text-anchor="middle" font-family="Poppins,Arial,sans-serif" font-weight="700" font-size="12" fill="var(--ink)">ACTION</text></svg>
  <p class="pillar-caption">Processes to Execute the<br>Vision</p>
</div>
<div class="pillar" style="left:692px">
  <svg width="116" height="128" viewBox="0 0 116 128"><polygon points="58,4 112,34 112,94 58,124 4,94 4,34" fill="#fff" stroke="var(--olive)" stroke-width="4"/><circle cx="48" cy="44" r="6" fill="var(--olive)"/><circle cx="68" cy="44" r="6" fill="var(--olive)"/><path d="M38 62c0-8 5-11 10-11s10 3 10 11zM58 62c0-8 5-11 10-11s10 3 10 11z" fill="var(--olive)"/><text x="58" y="82" text-anchor="middle" font-family="Poppins,Arial,sans-serif" font-weight="700" font-size="12" fill="var(--ink)">ACCOUNTA</text><text x="58" y="96" text-anchor="middle" font-family="Poppins,Arial,sans-serif" font-weight="700" font-size="12" fill="var(--ink)">BILITY</text></svg>
  <p class="pillar-caption">Tools and Checklists to<br>stay on Track</p>
</div>
<div class="pillar" style="left:871px">
  <svg width="116" height="128" viewBox="0 0 116 128"><polygon points="58,4 112,34 112,94 58,124 4,94 4,34" fill="#fff" stroke="var(--teal)" stroke-width="4"/><rect x="46" y="52" width="5" height="10" fill="var(--teal)"/><rect x="54" y="46" width="5" height="16" fill="var(--teal)"/><rect x="62" y="40" width="5" height="22" fill="var(--teal)"/><line x1="44" y1="63" x2="72" y2="63" stroke="var(--ink)" stroke-width="2"/><text x="58" y="89" text-anchor="middle" font-family="Poppins,Arial,sans-serif" font-weight="700" font-size="12" fill="var(--ink)">RESULTS</text></svg>
  <p class="pillar-caption">Dashboard &amp;<br>Metrics</p>
</div>

<div class="story-photo" role="img" aria-label="Photo of a handshake over a desk with a tablet and printed charts"></div>
<h2 class="story-title">OUR STORY</h2>
<div class="story-text">
  <p>Consectetur adipiscing elit, sed do eiusmod tempor incididunt ut labore et dolore magna aliqua. Ut enim ad minim veniam, quis nostrud exercitation ullamco. Duis aute irure dolor in reprehenderit in voluptate velit esse cillum dolore eu fugiat nulla pariatur. Excepteur sint occaecat cupidatat non proident, sunt in culpa qui officia deserunt mollit anim id est laborum.</p>
  <p>Duis aute irure dolor in reprehenderit in voluptate velit esse cillum dolore eu fugiat nulla pariatur. Excepteur sint occaecat cupidatat non proident, sunt in culpa qui officia deserunt mollit anim id est laborum.</p>
</div>
<a class="btn btn-blue" style="left:549px;top:1355px;width:98px;height:30px">Read more</a>

<h2 class="member-title">BECOME A QUIVL MEMBER TODAY</h2>
<p class="member-sub">and you will receive</p>

<div class="offer" style="left:132px">
  <div class="offer-photo" role="img" aria-label="Photo of a team meeting in a bright office" style="background:linear-gradient(135deg,#e8ecf1,#8795a8)"></div>
  <h3>QUIVL Coaching</h3>
  <ul><li>Coaching for your leadership team</li><li>Launch pad, Monthly and quarterly touchpoints</li><li>Continuous learning model</li></ul>
</div>
<div class="offer" style="left:454px">
  <div class="offer-photo" role="img" aria-label="Photo of a tablet showing the word ideas beside a coffee cup and glasses" style="background:linear-gradient(135deg,#b67a55,#d9c9b6 55%,#8e4b3a)"></div>
  <h3>QUIVL Structure</h3>
  <ul><li>Coaching for your leadership team</li><li>Launch pad, Monthly and quarterly touchpoints</li><li>Continuous learning model</li></ul>
</div>
<div class="offer" style="left:777px">
  <div class="offer-photo" role="img" aria-label="Illustration of a colourful tree of resource icons with a magnifying glass" style="background:linear-gradient(135deg,#f4f5f7,#c9d4de)"></div>
  <h3>QUIVL Resources</h3>
  <ul><li>Coaching for your leadership team</li><li>Launch pad, Monthly and quarterly touchpoints</li><li>Continuous learning model</li></ul>
</div>
<a class="btn btn-white" style="left:519px;top:1919px;width:124px;height:35px">Join now</a>

<h2 class="section-title" style="top:2050px;color:var(--ink);font-size:17px">OUR BLOG</h2>
<div class="blog-card" style="left:132px">
  <div class="blog-photo" role="img" aria-label="Photo of businessmen talking at a meeting table" style="background:linear-gradient(135deg,#c9cdd3,#6f7784)"></div>
  <h3>Explore Our Solutions / Services</h3>
  <p>Northvale Refrigeration is one of the leading commercial air conditioning installations companies in Central New York.</p>
</div>
<div class="blog-card" style="left:458px">
  <div class="blog-photo" role="img" aria-label="Photo of a tablet displaying sales charts on a desk" style="background:linear-gradient(135deg,#d7e7f3,#5d9fd0)"></div>
  <h3>Sales Services</h3>
  <p>We help convenience stores, grocery stores, and restaurants in Central New York and across the Northeast.</p>
</div>
<div class="blog-card" style="left:780px">
  <div class="blog-photo" role="img" aria-label="Photo of two consultants reviewing a laptop together" style="background:linear-gradient(135deg,#9fb0c4,#4b5d74)"></div>
  <h3>Strategic Consulting</h3>
  <p>Since the beginning, Northvale Refrigeration has prided itself on customer service. With over 60 trained technicians across the Northeast.</p>
</div>

<div class="quote-bar">
  <svg class="abs" style="left:28px;top:28px" width="32" height="32" viewBox="0 0 24 24"><path d="M6.6 10.8a15.1 15.1 0 0 0 6.6 6.6l2.2-2.2c.3-.3.7-.4 1-.2 1.1.4 2.3.6 3.6.6.6 0 1 .4 1 1V20c0 .6-.4 1-1 1A17 17 0 0 1 3 4c0-.6.4-1 1-1h3.5c.6 0 1 .4 1 1 0 1.3.2 2.5.6 3.6.1.3 0 .7-.2 1z" fill="var(--white)"/></svg>
  <p class="quote-label">Make an quote<br>call us :</p>
  <p class="quote-phone">833-555-0147</p>
  <div class="subscribe-field">
    <svg class="abs" style="left:14px;top:11px" width="13" height="10" viewBox="0 0 13 10"><rect width="13" height="10" rx="1" fill="#a0a5ab"/><path d="M0 1l6.5 5L13 1" fill="none" stroke="#fff" stroke-width="1.2"/></svg>
    Enter your mail address
  </div>
  <div class="subscribe-btn">Subscribe</div>
</div>

<div class="footer-col" style="left:139px">
  <h4>Navigation</h4>
  <ul class="footer-links"><li>About us</li><li>Blog</li><li>Membership</li><li>About us</li><li>Services</li></ul>
</div>
<div class="footer-col" style="left:366px">
  <h4>General Info</h4>
  <ul class="footer-links"><li>Home</li><li>Privacy Policy</li><li>Terms &amp; Conditions</li></ul>
</div>
<div class="footer-col office" style="left:580px">
  <h4>Office Info</h4>
  <ul>
    <li><svg width="12" height="12" viewBox="0 0 12 12"><path d="M12 0L0 5l5 2 2 5z" fill="var(--white)"/></svg><span>4820 Alder Road<br>Brookmere, NY 14620</span></li>
    <li><svg width="12" height="12" viewBox="0 0 24 24"><path d="M6.6 10.8a15.1 15.1 0 0 0 6.6 6.6l2.2-2.2c.3-.3.7-.4 1-.2 1.1.4 2.3.6 3.6.6.6 0 1 .4 1 1V20c0 .6-.4 1-1 1A17 17 0 0 1 3 4c0-.6.4-1 1-1h3.5c.6 0 1 .4 1 1 0 1.3.2 2.5.6 3.6.1.3 0 .7-.2 1z" fill="var(--white)"/></svg><span>833-555-0147</span></li>
    <li><svg width="12" height="10" viewBox="0 0 13 10"><rect width="13" height="10" rx="1" fill="var(--white)"/><path d="M0 1l6.5 5L13 1" fill="none" stroke="var(--footer)" stroke-width="1.2"/></svg><span>contact@quivl.com</span></li>
  </ul>
</div>
<div class="footer-col" style="left:813px">
  <h4>Social Links</h4>
  <div class="social"><span style="background:#3b9fd8"></span><span style="background:#3c5a99"></span><span style="background:#d44a3a"></span><span style="background:#c4302b"></span><span style="background:#6b7280"></span><span style="background:#3f729b"></span></div>
</div>

<div class="copyright">© 2018 quivl.com. All Rights Reserved.</div>

</body>
</html>
```